Box design for superfood powders

Hey,
I am creating a new brand of superfoods mixes in and I am looking for a designer to create the design for the box.
I have for 4 products on the roadmap, but I need the design just for the first one:
- For skin nails and hair benefits: Collagen + CoQ10 and Vitamin C powders (eg: Blueberries, Camu Camu, Acai)
- For energy and immune system (eg: mushrooms powder)
- Green Mix (eg: Spirulina + Wheatgrass + Chlorella)
- Protein mix (eg: hemp + rice powders)
I will use Kraft paper for the box so I am able to print max 2 colors on them (black and another color distinctive for each specific powder mix).
I need the design just for the first one with collagen, because all the products will have the same format. I will just change the name, ingredients and the color
More details in the archive attached.

Updates
Low design quality
Target Market(s)
woman between 30-50
Requirements
Should not have
- Ilustrations with fruits or flowers
Just shapes and colors

```html
<!DOCTYPE html>
<html lang="en">
<head>
<meta charset="utf-8">
<title>Radiant Collagen – box dieline</title>
<link rel="stylesheet" href="https://fonts.googleapis.com/css2?family=Poppins:wght@400;500;700&family=Archivo+Narrow:wght@400;700&display=swap">
<style>
  :root{
    --kraft:#c89d6e;
    --ink:#111111;
    --grey:#8b8782;
    --grey-light:#aaa59e;
    --rule:#9c978f;
    --cut:#5a4a3a;
    --paper:#ffffff;
  }
  html,body{margin:0;padding:0;width:1200px;height:697px;overflow:hidden;background:var(--paper);}
  .dieline{display:block;width:1200px;height:697px;}
  .board{fill:var(--kraft);stroke:var(--cut);stroke-width:0.8;}
  .corner-dark{fill:var(--grey);}
  .corner-light{fill:var(--grey-light);}
  .frame-line{fill:none;stroke:var(--rule);stroke-width:1.2;}
  .copy{font-family:"Poppins",sans-serif;fill:var(--ink);font-size:11.5px;}
  .copy-center{text-anchor:middle;}
  .brand-name{font-family:"Poppins",sans-serif;font-weight:500;font-size:15px;fill:var(--paper);text-anchor:middle;letter-spacing:1px;}
  .product-kicker{font-family:"Poppins",sans-serif;font-size:19px;fill:var(--ink);text-anchor:middle;}
  .product-name{font-family:"Poppins",sans-serif;font-weight:700;font-size:33px;fill:var(--ink);text-anchor:middle;}
  .flavour{font-family:"Poppins",sans-serif;font-size:10px;fill:var(--ink);text-anchor:middle;}
  .net-weight{font-family:"Poppins",sans-serif;font-size:11px;fill:var(--ink);text-anchor:middle;}
  .nf{font-family:"Archivo Narrow",sans-serif;fill:var(--ink);}
  .nf-title{font-size:25px;font-weight:700;}
  .nf-bold{font-weight:700;}
  .nf-rule{stroke:var(--ink);}
  .nf-right{text-anchor:end;}
  .badge{fill:none;stroke:var(--ink);stroke-width:1.6;}
  .badge-caption{font-family:"Poppins",sans-serif;font-size:7px;fill:#4a3e33;text-anchor:middle;}
</style>
</head>
<body>
<svg class="dieline" viewBox="-170 40 1653 960" preserveAspectRatio="xMidYMid meet" xmlns="http://www.w3.org/2000/svg" role="img" aria-label="Flat dieline of the Radiant Collagen box">
  <defs>
    <g id="panel-face">
      <polygon class="corner-light" points="80,0 102,0 0,118 0,92"/>
      <polygon class="corner-dark" points="0,0 80,0 0,92"/>
      <polygon class="corner-light" points="281,328 281,353 204,443 178,443"/>
      <polygon class="corner-dark" points="281,353 281,443 204,443"/>
      <polyline class="frame-line" points="180,24 262,24 262,380"/>
      <polyline class="frame-line" points="190,32 254,32 254,368"/>
      <polyline class="frame-line" points="20,60 20,420 100,420"/>
      <polyline class="frame-line" points="28,72 28,411 88,411"/>
    </g>
  </defs>

  <!-- top flaps -->
  <g class="flaps-top">
    <polygon class="board" points="95,322 107,100 355,100 371,322"/>
    <path class="board" d="M376,322 V100 H657 V322 Z"/>
    <path class="board" d="M376,100 V90 Q376,55 411,55 H622 Q657,55 657,90 V100 Z"/>
    <polygon class="board" points="662,322 677,100 926,100 937,322"/>
  </g>

  <!-- bottom flaps -->
  <g class="flaps-bottom">
    <polygon class="board" points="379,765 393,988 643,988 657,765"/>
    <rect class="board" x="657" y="765" width="281" height="223"/>
    <polygon class="board" points="941,765 953,988 1203,988 1218,765"/>
  </g>

  <!-- main faces -->
  <g class="faces">
    <rect class="board" x="95" y="322" width="281" height="443"/>
    <rect class="board" x="376" y="322" width="281" height="443"/>
    <rect class="board" x="657" y="322" width="281" height="443"/>
    <rect class="board" x="938" y="322" width="280" height="443"/>
    <use href="#panel-face" x="95" y="322"/>
    <use href="#panel-face" x="376" y="322"/>
    <use href="#panel-face" x="657" y="322"/>
    <use href="#panel-face" x="938" y="322"/>
  </g>

  <!-- ingredients panel -->
  <g class="panel-ingredients copy">
    <text x="147" y="382">INGREDIENTS:</text>
    <text x="147" y="410">Type 1 Marine Collagen</text>
    <text x="147" y="423">CoQ10</text>
    <text x="147" y="437">Hyaluronic acid powder</text>
    <text x="147" y="451">Camu Camu</text>
    <text x="147" y="464">Rosehip</text>
    <text x="147" y="478">Sea buckthorn</text>
    <text x="147" y="492">Banana</text>
    <text x="147" y="505">Date</text>
    <text x="147" y="519">Acai</text>
    <text x="147" y="541">We make it easy for busy</text>
    <text x="147" y="555">people to look and feel good</text>
    <text x="147" y="569">about their appearance. Just</text>
    <text x="147" y="582">add Radiant Collagen</text>
    <text x="147" y="596">powder to your favorite</text>
    <text x="147" y="610">smoothie or milk and get the</text>
    <text x="147" y="624">extra dose of collagen and</text>
    <text x="147" y="637">skin protecting antioxidants.</text>
    <text x="147" y="665">It helps combat the effects of</text>
    <text x="147" y="679">free radicals and may restore</text>
    <text x="147" y="693">your natural plumpness.</text>
  </g>

  <!-- front panel -->
  <g class="panel-front">
    <circle cx="516" cy="440" r="70" fill="var(--ink)"/>
    <text class="brand-name" x="516" y="445">VITALBLOOM</text>
    <text class="product-kicker" x="516" y="583">RADIANT</text>
    <text class="product-name" x="516" y="616">Collagen</text>
    <line x1="447" y1="637" x2="585" y2="637" stroke="var(--ink)" stroke-width="1.6"/>
    <text class="flavour" x="516" y="651">BLUEBERRIES, CAMU</text>
    <text class="flavour" x="516" y="664">CAMU, ACAI</text>
    <line x1="447" y1="671" x2="585" y2="671" stroke="var(--ink)" stroke-width="1.6"/>
    <text class="net-weight" x="516" y="698">14 portions x 10g = 140g</text>
  </g>

  <!-- nutrition panel -->
  <g class="panel-nutrition nf">
    <rect x="705" y="388" width="184" height="332" fill="none" stroke="var(--ink)" stroke-width="1"/>
    <text class="nf-title" x="709" y="412">Nutrition Facts</text>
    <line class="nf-rule" x1="709" y1="416" x2="885" y2="416" stroke-width="0.8"/>
    <text x="709" y="427" font-size="10">4 servings per container</text>
    <text class="nf-bold" x="709" y="439" font-size="10.5">Serving size</text>
    <text class="nf-bold nf-right" x="885" y="439" font-size="10.5">1 cup (180g)</text>
    <line class="nf-rule" x1="709" y1="447" x2="885" y2="447" stroke-width="6"/>
    <text class="nf-bold" x="709" y="462" font-size="6.5">Amount per serving</text>
    <text class="nf-bold" x="709" y="480" font-size="19">Calories</text>
    <text class="nf-bold nf-right" x="885" y="481" font-size="22">245</text>
    <line class="nf-rule" x1="709" y1="486" x2="885" y2="486" stroke-width="3.5"/>
    <text class="nf-bold nf-right" x="885" y="496" font-size="6.5">% Daily Value*</text>
    <g font-size="8.5">
      <line class="nf-rule" x1="709" y1="500" x2="885" y2="500" stroke-width="0.6"/>
      <text x="709" y="510"><tspan class="nf-bold">Total Fat</tspan> 12g</text><text class="nf-bold nf-right" x="885" y="510">14%</text>
      <line class="nf-rule" x1="709" y1="513" x2="885" y2="513" stroke-width="0.6"/>
      <text x="721" y="523">Saturated Fat 2g</text><text class="nf-bold nf-right" x="885" y="523">10%</text>
      <line class="nf-rule" x1="709" y1="526" x2="885" y2="526" stroke-width="0.6"/>
      <text x="721" y="536" font-style="italic">Trans Fat 0g</text>
      <line class="nf-rule" x1="709" y1="539" x2="885" y2="539" stroke-width="0.6"/>
      <text x="709" y="549"><tspan class="nf-bold">Cholesterol</tspan> 8mg</text><text class="nf-bold nf-right" x="885" y="549">3%</text>
      <line class="nf-rule" x1="709" y1="552" x2="885" y2="552" stroke-width="0.6"/>
      <text x="709" y="562"><tspan class="nf-bold">Sodium</tspan> 210mg</text><text class="nf-bold nf-right" x="885" y="562">9%</text>
      <line class="nf-rule" x1="709" y1="565" x2="885" y2="565" stroke-width="0.6"/>
      <text x="709" y="575"><tspan class="nf-bold">Total Carbohydrate</tspan> 34g</text><text class="nf-bold nf-right" x="885" y="575">12%</text>
      <line class="nf-rule" x1="709" y1="578" x2="885" y2="578" stroke-width="0.6"/>
      <text x="721" y="588">Dietary Fiber 7g</text><text class="nf-bold nf-right" x="885" y="588">25%</text>
      <line class="nf-rule" x1="709" y1="591" x2="885" y2="591" stroke-width="0.6"/>
      <text x="721" y="601">Total Sugars 5g</text>
      <line class="nf-rule" x1="733" y1="604" x2="885" y2="604" stroke-width="0.6"/>
      <text x="733" y="614">Includes 4g Added Sugars</text><text class="nf-bold nf-right" x="885" y="614">8%</text>
      <line class="nf-rule" x1="709" y1="617" x2="885" y2="617" stroke-width="0.6"/>
      <text x="709" y="627" class="nf-bold">Protein <tspan font-weight="400">11g</tspan></text>
      <line class="nf-rule" x1="709" y1="633" x2="885" y2="633" stroke-width="6"/>
      <text x="709" y="647">Vitamin D 4mcg</text><text class="nf-right" x="885" y="647">20%</text>
      <line class="nf-rule" x1="709" y1="650" x2="885" y2="650" stroke-width="0.6"/>
      <text x="709" y="660">Calcium 210mg</text><text class="nf-right" x="885" y="660">16%</text>
      <line class="nf-rule" x1="709" y1="663" x2="885" y2="663" stroke-width="0.6"/>
      <text x="709" y="673">Iron 4mg</text><text class="nf-right" x="885" y="673">22%</text>
      <line class="nf-rule" x1="709" y1="676" x2="885" y2="676" stroke-width="0.6"/>
      <text x="709" y="686">Potassium 380mg</text><text class="nf-right" x="885" y="686">8%</text>
    </g>
    <line class="nf-rule" x1="709" y1="690" x2="885" y2="690" stroke-width="3"/>
    <g font-size="6.4">
      <text x="709" y="699">*The % Daily Value (DV) tells you how much a nutrient</text>
      <text x="713" y="707">in a serving of food contributes to a daily diet. 2,000</text>
      <text x="713" y="715">calories a day is used for general nutrition advice.</text>
    </g>
  </g>

  <!-- info panel -->
  <g class="panel-info">
    <g class="badges">
      <circle class="badge" cx="1022" cy="382" r="13"/>
      <circle class="badge" cx="1070" cy="382" r="13"/>
      <circle class="badge" cx="1126" cy="382" r="13"/>
      <circle class="badge" cx="1022" cy="427" r="13"/>
      <circle class="badge" cx="1070" cy="427" r="13"/>
      <circle class="badge" cx="1126" cy="427" r="13"/>
      <circle class="badge" cx="1022" cy="472" r="13"/>
      <circle class="badge" cx="1070" cy="472" r="13"/>
      <circle class="badge" cx="1126" cy="472" r="13"/>
      <text class="badge-caption" x="1022" y="404">Gluten Free</text>
      <text class="badge-caption" x="1070" y="404">Lactose Free</text>
      <text class="badge-caption" x="1126" y="404">Kosher Certified</text>
      <text class="badge-caption" x="1022" y="449">Non GMO</text>
      <text class="badge-caption" x="1070" y="449">Lactose Free</text>
      <text class="badge-caption" x="1126" y="449">Kosher Certified</text>
      <text class="badge-caption" x="1022" y="494">Gluten Free</text>
      <text class="badge-caption" x="1070" y="494">Lactose Free</text>
      <text class="badge-caption" x="1126" y="494">Kosher Certified</text>
    </g>
    <g class="copy">
      <text x="995" y="522">How to use it: Add one pack to</text>
      <text x="995" y="535">your water, smoothies, yoghurt,</text>
      <text x="995" y="548">musli, oatmeal</text>
      <text x="995" y="572">Storage: Keep closed in a cool</text>
      <text x="995" y="585">dry place</text>
      <text x="995" y="610">Produced by. Norvale SRL for</text>
      <text x="995" y="623">Brightmix SRL</text>
      <text x="995" y="647">Connect:</text>
      <text x="995" y="660">Call +00 000 0000 000 or</text>
      <text x="995" y="685">visit our website</text>
      <text x="995" y="698">www.vitalbloom-mix.com/start</text>
      <text x="995" y="710">Nutrition Value table</text>
    </g>
  </g>
</svg>
</body>
</html>
```